Flyer Design Project

I am starting a new Cake Business called "SWEET TIN JOY" and want flyers. The main product are Cupcakes and will be marketed for parties/events/celebrations to order. Other cakes can be made to order (Christmas/Birthday etc)

Industry/Entity Type

Business

Requirements
Must have
• Contact Telephone Number

```html
<!DOCTYPE html>
<html lang="en">
<head>
<meta charset="utf-8">
<title>Sweet Tin Joy – Flyer</title>
<link href="https://fonts.googleapis.com/css2?family=Fredoka:wght@500;600&family=Lobster&family=Ubuntu:wght@400;500;700&display=swap" rel="stylesheet">
<style>
  :root{
    --paper:#ffffff;
    --brown:#8a5522;
    --brown-deep:#6b3a12;
    --brown-dark:#4a230c;
    --maroon:#5a1f0b;
    --gold:#f4c430;
    --parchment-light:#fbe7a6;
    --parchment:#f0c866;
    --heading:#b0520e;
    --ink:#2b1a0b;
    --white:#ffffff;
  }
  *{margin:0;padding:0;box-sizing:border-box}
  html,body{width:900px;height:1200px;overflow:hidden;background:var(--paper)}
  .flyer{position:relative;width:900px;height:1200px;overflow:hidden}
  .abs{position:absolute}

  .top-band{left:35px;top:33px;width:830px;height:304px;
    background:linear-gradient(160deg,var(--brown) 0%,#7c4a1b 55%,var(--brown-deep) 100%)}
  .quality-strip{left:490px;top:88px;width:375px;height:108px;background:rgba(90,40,10,.75)}
  .brand-name{left:108px;top:180px;width:330px;text-align:center;white-space:nowrap;
    font:500 45px/1 "Ubuntu",sans-serif;color:var(--white);z-index:2}
  .brand-tag{left:148px;top:246px;font:26px/1 "Lobster",cursive;color:var(--white)}

  .quality{right:103px;top:98px;text-align:right;color:var(--white)}
  .quality .q1{font:500 27px/1.05 "Fredoka",sans-serif}
  .quality .q2{font:40px/1 "Lobster",cursive}
  .quality .q3{font:500 23px/1.1 "Fredoka",sans-serif}

  .photo-main{left:35px;top:357px;width:375px;height:628px;
    background:radial-gradient(circle at 40% 45%,#f4a9bd 0%,#d97b8f 28%,#8c3a2a 60%,#4a1d10 100%)}
  .parchment{left:410px;top:357px;width:455px;height:560px;
    background:radial-gradient(circle at 55% 45%,var(--parchment-light) 0%,var(--parchment) 75%,#e2a93e 100%)}
  .footer{left:35px;top:985px;width:830px;height:182px;
    background:linear-gradient(180deg,#5a2d10 0%,var(--brown-dark) 60%,#3a1a08 100%)}

  .copy{left:557px;width:252px;color:var(--ink)}
  .copy h2{font:600 29px/1 "Fredoka",sans-serif;color:var(--heading);margin-bottom:8px;margin-left:-4px}
  .copy p{font:400 14.2px/18.6px "Ubuntu",sans-serif}
  .copy-one{top:486px}
  .copy-two{top:679px}

  .exclusive{left:580px;top:905px;width:230px;text-align:center;font-family:"Lobster",cursive;line-height:1}
  .exclusive .e1{font-size:32px;color:var(--white)}
  .exclusive .e2{font-size:46px;color:var(--gold);margin-top:-2px}
  .exclusive .e3{font-size:22px;color:var(--white);margin-top:2px}

  .contact{left:90px;top:1034px;font:700 20px/27px "Ubuntu",sans-serif;font-style:normal;color:var(--white)}

  .tile-photo{position:absolute;width:132px;height:132px;border-radius:20px}
  .tile-one{left:362px;top:305px;transform:rotate(8deg);background:radial-gradient(circle,#f3efe0 0%,#b8d9b8 50%,#7a4a3a 100%)}
  .tile-two{left:362px;top:534px;transform:rotate(-6deg);background:radial-gradient(circle,#f39bbf 0%,#e0699a 45%,#7fc7b0 100%)}
  .tile-three{left:362px;top:763px;transform:rotate(7deg);background:radial-gradient(circle,#ffffff 0%,#f1e6df 35%,#c8242a 70%,#8a1418 100%)}
</style>
</head>
<body>
<main class="flyer">
  <div class="abs top-band"></div>
  <div class="abs quality-strip"></div>
  <div class="abs brand-name">SWEET TIN JOY</div>
  <div class="abs brand-tag">Mega Restaurant</div>

  <div class="abs quality">
    <div class="q1">Hi-Quality</div>
    <div class="q2">Mega Restaurant</div>
    <div class="q3">in the City...</div>
  </div>

  <div class="abs photo-main" role="img" aria-label="Close-up photo of a pink-frosted cupcake with a lime slice and gold cutlery"></div>
  <div class="abs parchment"></div>
  <div class="abs footer"></div>

  <svg class="abs" style="left:0;top:0" width="900" height="1200" viewBox="0 0 900 1200" aria-hidden="true">
    <defs>
      <linearGradient id="goldEdge" x1="0" y1="0" x2="0" y2="1">
        <stop offset="0" stop-color="#f7d98a"/><stop offset="1" stop-color="#c8922e"/>
      </linearGradient>
    </defs>
    <rect x="35" y="337" width="830" height="20" fill="url(#goldEdge)"/>
    <rect x="35" y="341" width="830" height="12" fill="#fffaf0"/>
    <rect x="410" y="357" width="22" height="628" fill="url(#goldEdge)"/>
    <rect x="414" y="357" width="14" height="628" fill="#fffaf0"/>
    <path d="M560 917 Q575 880 615 880 L865 880 L865 1000 L540 1000 Z" fill="#3f1c08"/>
    <path d="M35 992 L500 992 Q545 992 555 950 L565 912 Q575 880 615 880 L865 880" fill="none" stroke="url(#goldEdge)" stroke-width="24"/>
    <path d="M35 992 L500 992 Q545 992 555 950 L565 912 Q575 880 615 880 L865 880" fill="none" stroke="#fffaf0" stroke-width="14"/>

    <circle cx="680" cy="340" r="122" fill="#fffaf0"/>
    <circle cx="680" cy="340" r="114" fill="var(--maroon)"/>
    <circle cx="680" cy="340" r="106" fill="none" stroke="#c9a070" stroke-width="1.5" stroke-dasharray="5 4"/>

    <g>
      <rect x="340" y="283" width="176" height="176" rx="30" fill="url(#goldEdge)" transform="rotate(8 428 371)"/>
      <rect x="350" y="293" width="156" height="156" rx="24" fill="#fffaf0" transform="rotate(8 428 371)"/>
      <rect x="340" y="512" width="176" height="176" rx="30" fill="url(#goldEdge)" transform="rotate(-6 428 600)"/>
      <rect x="350" y="522" width="156" height="156" rx="24" fill="#fffaf0" transform="rotate(-6 428 600)"/>
      <rect x="340" y="741" width="176" height="176" rx="30" fill="url(#goldEdge)" transform="rotate(7 428 829)"/>
      <rect x="350" y="751" width="156" height="156" rx="24" fill="#fffaf0" transform="rotate(7 428 829)"/>
    </g>
    <g font-family="Fredoka, sans-serif" font-weight="600" fill="#8a3a10">
      <g transform="rotate(-8 485 465)">
        <rect x="456" y="438" width="58" height="56" rx="8" fill="#f2cf7a" stroke="#c8922e" stroke-width="2"/>
        <text x="485" y="476" font-size="22" text-anchor="middle"><tspan font-size="14">$</tspan>27</text>
      </g>
      <g transform="rotate(-8 367 700)">
        <rect x="338" y="673" width="58" height="56" rx="8" fill="#f2cf7a" stroke="#c8922e" stroke-width="2"/>
        <text x="367" y="711" font-size="22" text-anchor="middle"><tspan font-size="14">$</tspan>18</text>
      </g>
      <g transform="rotate(-8 488 925)">
        <rect x="459" y="898" width="58" height="56" rx="8" fill="#f2cf7a" stroke="#c8922e" stroke-width="2"/>
        <text x="488" y="936" font-size="22" text-anchor="middle"><tspan font-size="14">$</tspan>13</text>
      </g>
    </g>
    <g font-family="Fredoka, sans-serif" font-weight="600" text-anchor="middle">
      <text x="682" y="306" font-size="34" fill="#fff">we</text>
      <text x="682" y="356" font-size="54" fill="var(--gold)">waiting</text>
      <text x="682" y="392" font-size="32" fill="#fff">for you!</text>
    </g>
  </svg>

  <div class="tile-photo tile-one" role="img" aria-label="Cupcake with white frosting and mint sugar roses"></div>
  <div class="tile-photo tile-two" role="img" aria-label="Row of cupcakes topped with pink sugar roses"></div>
  <div class="tile-photo tile-three" role="img" aria-label="Round white Christmas cake with red ribbon"></div>

  <section class="abs copy copy-one">
    <h2>heading one</h2>
    <p>This is the details text for your heading title. This is the details text for your heading title. This is the details text for your heading title. This is the details text for your heading title. This is the details text for your heading title.</p>
  </section>
  <section class="abs copy copy-two">
    <h2>heading two</h2>
    <p>This is the details text for your heading title. This is the details text for your heading title. This is the details text for your heading title.</p>
  </section>

  <div class="abs exclusive">
    <div class="e1">Get it</div>
    <div class="e2">Exclusive</div>
    <div class="e3">to Better Services</div>
  </div>

  <address class="abs contact">
    Your Company Address Tex Here in Detailed.<br>
    Phone: 0123 456 789, Fax: 0123 456 789<br>
    Email: mymail@domain.com, Website: mywebsite.com
  </address>
</main>
</body>
</html>
```